Home Inspection Postcard Design

Home inspection. Attached is my old postcard. I would like the card to have the same verbage on it - front and back. but I would like the house graphic and the colors to be blues. The only changes to the information is the website address is www.brambleridgehi.com. THe PO Box is now 718 rather than 369, and I wanted to add my email address which is brambleridgehi@mailvexo.net. I would like to keep the $25 off box but add "or a 10% military discount, which ever is greater" or something like that .If you could mock something up for me I would really appreciate it. I would also like a glossy finish on the cards

```html
<!DOCTYPE html>
<html lang="en">
<head>
<meta charset="utf-8">
<title>Bramble Ridge Home – Inspection Postcard</title>
<link rel="stylesheet" href="https://fonts.googleapis.com/css2?family=Open+Sans:ital,wght@0,400;0,600;0,700;1,700;1,800&family=Pinyon+Script&display=swap">
<style>
:root{
  --bg:#8a5a36;
  --card:#ffffff;
  --red:#e4432a;
  --red-dark:#c8311d;
  --navy:#1d3a73;
  --navy-deep:#152c5c;
  --blue:#1f56a8;
  --ink:#2b2b2b;
  --grey-box:#e6e6e6;
}
*{margin:0;padding:0;box-sizing:border-box}
html,body{width:907px;height:1200px;overflow:hidden}
body{background:var(--bg);font-family:"Open Sans",Arial,sans-serif;color:var(--ink);position:relative}
.card{position:absolute;left:96px;width:715px;height:556px;background:var(--card);overflow:hidden}
.card--front{top:28px}
.card--back{top:605px;height:557px}

/* front */
.top-band{position:absolute;left:0;top:0;width:715px;height:104px;background:linear-gradient(90deg,var(--red-dark),var(--red))}
.headline{position:absolute;right:18px;top:30px;color:#fff;font-weight:800;font-style:italic;font-size:35px;letter-spacing:-.3px;line-height:1}
.tagline{position:absolute;right:18px;top:74px;color:#fff;font-family:"Pinyon Script",cursive;font-size:17px}
.hero-photo{position:absolute;left:0;top:104px;width:430px;height:380px;
  background:linear-gradient(180deg,#c7d1db 0%,#a7aab0 30%,#8e8a86 55%,#5f7f34 75%,#4a7325 100%)}
.hero-fade{position:absolute;left:250px;top:104px;width:185px;height:380px;background:linear-gradient(90deg,rgba(255,255,255,0),#fff)}
.pitch{position:absolute;left:416px;top:108px;width:290px}
.pitch h2{color:var(--navy);font-size:18.5px;font-weight:700;margin-bottom:4px}
.pitch p{font-size:11.2px;line-height:15px;margin-bottom:7px}
.offer{position:absolute;left:416px;top:328px;width:299px;height:50px;background:var(--grey-box);border:1px dashed var(--red);display:flex;align-items:center;padding-left:6px}
.offer__amount{color:var(--blue);font-weight:700;font-size:37px;line-height:1;margin-right:8px}
.offer__note{font-size:13px;line-height:15px;color:var(--ink);font-weight:600}
.military{position:absolute;left:420px;top:384px;font-size:12.4px}
.military b{color:var(--blue)}

.wave{position:absolute;left:0;bottom:0;width:715px;height:150px}
.brand-disc{position:absolute;width:126px;height:126px;border-radius:50%;background:#fff;border:3px solid #e1e1e1;box-shadow:0 2px 6px rgba(0,0,0,.25);display:flex;align-items:center;justify-content:center;text-align:center}
.brand-disc span{color:var(--navy);font-weight:700;font-size:15px;line-height:18px}
.card--front .brand-disc{left:30px;top:405px}
.contact{position:absolute;color:#fff;font-size:12px;font-weight:600;line-height:18px}
.contact .ico{display:inline-block;width:8px;height:8px;background:var(--red);border-radius:50%;vertical-align:middle;margin:0 5px}
.front-phone{right:280px;top:496px;text-align:right}
.front-office{right:20px;top:458px;text-align:right;font-size:11px;line-height:15px}
.front-office h3{font-size:16.5px;font-weight:600;margin-bottom:4px}
.front-office .web{font-size:11.5px;margin-top:6px;display:block}

/* back */
.yard-photo{position:absolute;left:0;top:0;width:372px;height:186px;
  background:linear-gradient(180deg,#5c86c2 0%,#9ab7d8 35%,#e8ecee 55%,#c9cbc7 72%,#4e8a37 90%,#3e7a2c 100%)}
.question{position:absolute;left:0;top:186px;width:372px;height:31px;background:var(--red);color:#fff;font-size:18px;font-weight:700;padding:3px 0 0 17px}
.explainer{position:absolute;left:17px;top:222px;width:340px;font-size:10.7px;line-height:15.6px;text-align:justify}
.stamp{position:absolute;left:626px;top:42px;width:64px;height:64px;border:1.5px solid #333}
.address-line{position:absolute;left:475px;width:224px;border-top:1.5px solid #555}
.back-office{left:17px;top:466px;font-size:11px;line-height:17px}
.back-office h3{font-size:16.5px;font-weight:600;margin-bottom:8px}
.back-office div{margin-left:2px}
.back-phone{left:263px;top:508px;font-size:11.5px;line-height:20px}
.card--back .brand-disc{left:542px;top:432px}
</style>
</head>
<body>

<section class="card card--front">
  <div class="top-band"></div>
  <div class="headline">We Leave No Stone Unturned</div>
  <div class="tagline">Licensed, Certified &amp; Insured</div>
  <div class="hero-photo" role="img" aria-label="Two-storey house with lit windows, garage doors and a green front lawn at dusk"></div>
  <div class="hero-fade"></div>

  <div class="pitch">
    <h2>Confidence In Home BUYING</h2>
    <p>Enjoy the comfort of peace-of-mind before buying your new home. Our trained professionals inspect the property and imediately present you with a detailed, yet clear report. They will answer any questions you may have.</p>
    <p>Join our expenenced inspectors in their tour of the property. They will acquaint you with its strenghts and weekness. You will feel confident in their judgement and throughness. Many Realtors, Sellers, Home Buyers, Mortgage companies and relocation companies have used our comprehensive report and services to their satisfaction.</p>
  </div>

  <div class="offer"><span class="offer__amount">$25 Off</span><span class="offer__note">Services<br>with this postcard</span></div>
  <div class="military">or a <b>10%</b> military discount, which ever is greater</div>

  <svg class="wave" viewBox="0 0 715 150" preserveAspectRatio="none" aria-hidden="true">
    <path d="M0 70 C180 110 420 20 715 8 L715 150 L0 150Z" fill="#fff"/>
    <path d="M0 60 C200 100 430 8 715 0 L715 14 C440 24 200 112 0 76Z" fill="var(--red)"/>
    <path d="M0 88 C200 120 440 36 715 30 L715 150 L0 150Z" fill="var(--navy)"/>
  </svg>

  <div class="brand-disc"><span>Bramble Ridge<br>Home</span></div>

  <div class="contact front-phone">912-555-0148<span class="ico"></span><br>brambleridgehi@mailvexo.net<span class="ico"></span></div>
  <div class="contact front-office">
    <h3>Bramble Ridge Home</h3>
    Bramble Ridge Home Inspection Services<span class="ico"></span><br>P.O box no.718<span class="ico" style="visibility:hidden"></span>
    <span class="web">www.brambleridgehi.com<span class="ico"></span></span>
  </div>
</section>

<section class="card card--back">
  <div class="yard-photo" role="img" aria-label="White house with a foreclosure home-for-sale sign on the front lawn"></div>
  <div class="question">Why Do I Need An Inspection?</div>
  <p class="explainer">The purchase of home or comercial building is one of the largest single investments you will ever make. You should know what to expect - in terms of needed and possible repairs and maintenance. A fresh coat of paint could be hiding serious problems. Stains on the ceiling may indicate a chronic roof leak or may be simply the result of a sinle incident. The inspector reviews these and other clues, then presents a professional opinion as to the condision of the property to help you avoid unpleasant surprises afterward. Ofcourse, an inspection may also point out the positive aspects of a building, as well as the type of maintenance needed to keep it in proper shape. After the inspection, you will have a much clearer understanding of the property, and be able to make you purchasing decision confidently.</p>

  <div class="stamp"></div>
  <div class="address-line" style="top:199px"></div>
  <div class="address-line" style="top:238px"></div>
  <div class="address-line" style="top:277px"></div>

  <svg class="wave" viewBox="0 0 715 150" preserveAspectRatio="none" aria-hidden="true">
    <path d="M0 40 C220 0 470 60 715 40 L715 150 L0 150Z" fill="#fff"/>
    <path d="M0 28 C220 -8 470 60 715 36 L715 52 C470 78 220 14 0 44Z" fill="var(--red)"/>
    <path d="M0 56 C220 24 470 88 715 66 L715 150 L0 150Z" fill="var(--navy)"/>
  </svg>

  <div class="contact back-office">
    <h3>Bramble Ridge Home</h3>
    <div><span class="ico" style="margin-left:0"></span>Bramble Ridge Home Inspection Services<br><span class="ico" style="visibility:hidden;margin-left:0"></span>P.O box no.718</div>
    <div style="margin-top:4px"><span class="ico" style="margin-left:0"></span>www.brambleridgehi.com</div>
  </div>
  <div class="contact back-phone"><span class="ico" style="margin-left:0"></span>912-555-0148<br><span class="ico" style="margin-left:0"></span>brambleridgehi@mailvexo.net</div>

  <div class="brand-disc"><span>Bramble Ridge<br>Home</span></div>
</section>

</body>
</html>
```